Tallowmere Coffee Company

Logo and coffee packaging design for a new coffee roasting company. Our plan is to small batch, craft roast coffee with $1 for each pound sold donated to non-profit rescue dog operations. Web address will be tallowmerecoffee.example
Prefer a logo with a Jack Russell Terrier or similar dog.....like the little ZVT dog or Torvin on the sitcom Quillmore.
Ideally we would have one package/bag for all our coffees with a place to put a sticker for the type coffee (origin, roast style etc) and maybe a sticker for the back or side with the story of a specific rescue dog associated with that roast.
Would like some strong color science based designs to make our product pop on the shelf.

```html
<!DOCTYPE html>
<html lang="en">
<head>
<meta charset="utf-8">
<title>Tallowmere Coffee – Bag Front</title>
<link rel="stylesheet" href="https://fonts.googleapis.com/css2?family=Passion+One:wght@700&family=Crete+Round&family=Lora:ital,wght@0,700;1,400&family=Open+Sans:wght@700&display=swap">
<style>
  :root {
    --stage: #d9d9d9;
    --bag-brown: #5c3511;
    --bean-orange: #f7ad3c;
    --bean-orange-light: #fbbf55;
    --cream: #efdca2;
    --cream-light: #f4e6b4;
    --ink-brown: #4a2a0e;
    --label-brown: #6b3c10;
  }
  html, body {
    margin: 0;
    width: 1200px;
    height: 1000px;
    overflow: hidden;
    background: var(--stage);
  }
  .bag-front {
    position: absolute;
    left: 360px;
    top: 25px;
    width: 480px;
    height: 950px;
    display: block;
  }
  .brand-mark, .product-name { font-family: "Passion One", Impact, sans-serif; }
  .tagline { font-family: "Crete Round", Georgia, serif; }
  .origin-serif { font-family: "Lora", Georgia, serif; }
  .origin-sans { font-family: "Open Sans", Arial, sans-serif; }
</style>
</head>
<body>
<svg class="bag-front" viewBox="0 0 472 935" xmlns="http://www.w3.org/2000/svg">
  <defs>
    <linearGradient id="bean-field" x1="0" y1="0" x2="0" y2="1">
      <stop offset="0" stop-color="var(--bean-orange-light)"/>
      <stop offset="1" stop-color="var(--bean-orange)"/>
    </linearGradient>
    <path id="tagline-curve" d="M88 543 Q232 500 378 550"/>
  </defs>

  <!-- bag body -->
  <rect class="bag-body" x="0" y="0" width="472" height="935" fill="var(--bag-brown)"/>

  <!-- bottle-shaped orange field (bean pattern area) -->
  <path class="bean-field" role="img" aria-label="Coffee bean pattern"
        d="M112 215 H360 Q380 215 380 235 V470 Q380 505 452 512 V750 Q380 758 380 790 V935 H92 V790 Q92 758 20 750 V512 Q92 505 92 470 V235 Q92 215 112 215 Z"
        fill="url(#bean-field)"/>

  <!-- hanging ribbon with brand -->
  <path class="brand-ribbon" d="M158 0 H328 V372 L243 322 L158 372 Z" fill="var(--cream)"/>
  <circle class="brand-dot" cx="243" cy="180" r="18" fill="var(--ink-brown)"/>
  <text class="brand-mark" x="243" y="238" text-anchor="middle" font-size="25" fill="var(--ink-brown)">TALLOWMERE</text>
  <text class="brand-mark" x="243" y="268" text-anchor="middle" font-size="30" fill="var(--ink-brown)">COFFEE</text>

  <!-- product name -->
  <text class="product-name" x="236" y="483" text-anchor="middle" font-size="104"
        textLength="340" lengthAdjust="spacingAndGlyphs"
        fill="var(--cream-light)" stroke="var(--ink-brown)" stroke-width="9"
        stroke-linejoin="round" paint-order="stroke">VELMARO</text>

  <!-- tagline -->
  <text class="tagline" font-size="29" fill="var(--cream-light)" stroke="var(--ink-brown)"
        stroke-width="5" stroke-linejoin="round" paint-order="stroke">
    <textPath href="#tagline-curve" startOffset="50%" text-anchor="middle">craft roast coffee</textPath>
  </text>

  <!-- origin label -->
  <path class="origin-label" d="M65 592 Q232 538 399 592 V724 H65 Z"
        fill="var(--cream)" stroke="var(--ink-brown)" stroke-width="7" stroke-linejoin="round"/>
  <text class="origin-serif" x="232" y="605" text-anchor="middle" font-size="23" font-style="italic" fill="var(--ink-brown)">from</text>
  <text class="origin-serif" x="232" y="651" text-anchor="middle" font-size="42" font-weight="700"
        fill="var(--label-brown)" stroke="var(--bean-orange)" stroke-width="3" paint-order="stroke">Colombia</text>
  <text class="origin-sans" x="232" y="673" text-anchor="middle" font-size="15" fill="var(--ink-brown)">Colombian Supremo</text>
  <ellipse class="flavor-oval" cx="232" cy="699" rx="76" ry="17" fill="var(--bean-orange)" stroke="var(--ink-brown)" stroke-width="2"/>
  <text class="origin-serif" x="232" y="704" text-anchor="middle" font-size="14" fill="var(--ink-brown)">Jalapeno Chocolate</text>

  <!-- net weight and web -->
  <text class="origin-sans" x="236" y="808" text-anchor="middle" font-size="15" fill="var(--ink-brown)">Net Wt. 12 oz.(340g)</text>
  <text class="origin-serif" x="236" y="827" text-anchor="middle" font-size="11" font-style="italic" font-weight="700" fill="var(--ink-brown)">www.tallowmerecoffee.example</text>
</svg>
</body>
</html>
```